Lakemont Harmony Medical Tri-Fold Flyer

a marketing 3- fold flyer for primary business awareness. this should offer all aspects of our medical practice. I have provided several pictures as well as all pertinent information needed to make a successful flyer. This needs to be eye catching and attractive. each page should feature something of its own.
my thoughts:
page 1- photo of office our mission statement and maybe our phone number and address
page 2- our LHM A-team flyer
page 3- our paragraph on our practice as well as some of our services. say something like we offer a wide scope of services including health coaching, weight loss. A "patient services coordinator" will help you pick out what services we can do for you. a pic
page 4- doctors bio and pics and logos
page 5-
page 6- our map our address and phone numbers. the sentence on making an appointment. our web page and facebook as well as our logos

Target Market(s)

we are a medical practice, so we are seeking new patients

Industry/Entity Type

Health Care

Font styles to use
Serif

Colors
34a6d7
33b8a4
abd036
fbee3e

Requirements
Must have
• I have enclosed a tri-fold info attachment as well as other pieces. Use what you feel will make our flyer attractive. Not too busy. Please try to get most info in
• All work purchased should be delivered with the PDF form for future changes by owner of medical office.
Nice to have
• All Info provided

```html
<!DOCTYPE html>
<html lang="en">
<head>
<meta charset="utf-8">
<title>Lakemont Harmony Medical – Tri-Fold Outside</title>
<link href="https://fonts.googleapis.com/css2?family=Cinzel:wght@400;600&family=Open+Sans:wght@400;600;700&family=Quicksand:wght@400;700&family=Tinos&display=swap" rel="stylesheet">
<style>
  :root{
    --bg:#6b6b6b;
    --paper:#ffffff;
    --sky-top:#e9f7fb;
    --sky-mid:#bde7f3;
    --sky-deep:#8fd4e8;
    --teal:#33b8c4;
    --blue:#1b8fd6;
    --deep-blue:#1c73c2;
    --heading-teal:#179aa8;
    --ink:#2b2b2b;
    --grey-row:#a9a9a9;
  }
  *{box-sizing:border-box;margin:0;padding:0}
  html,body{width:1200px;height:1200px;overflow:hidden}
  body{background:var(--bg);font-family:"Open Sans",sans-serif;color:var(--ink);position:relative}
  .brochure{position:absolute;left:60px;top:183px;width:1080px;height:834px;display:flex;box-shadow:0 20px 40px rgba(0,0,0,.35)}
  .panel{position:relative;width:360px;height:834px;overflow:hidden;background:var(--paper)}
  .panel + .panel{border-left:1px solid rgba(0,0,0,.06)}
  .wave{position:absolute;left:0;bottom:0;width:360px}
  .photo{position:absolute}

  /* panel: about */
  .about{background:linear-gradient(#f3f8fb,#fff 40%)}
  .about h2{position:absolute;left:22px;top:22px;font-family:"Tinos",serif;font-weight:400;font-size:24px;color:var(--heading-teal);letter-spacing:.5px}
  .about .sub{position:absolute;left:22px;top:52px;font-family:"Tinos",serif;font-size:15px;color:var(--deep-blue)}
  .about .copy{position:absolute;left:22px;top:90px;width:316px;font-size:9.6px;line-height:1.45;text-align:justify;color:#333}
  .about .copy p{margin-bottom:10px}
  .about .copy .tail{margin-left:118px}
  .about .photo{left:0;top:372px;width:360px;height:380px;background:linear-gradient(160deg,#eaf1e6 0%,#c9d9c0 40%,#d7c3a5 75%,#9bb84a 100%)}

  /* panel: contact */
  .contact{background:linear-gradient(#dff3f9,var(--sky-mid) 45%,var(--sky-deep))}
  .hours-title{position:absolute;left:0;right:0;top:178px;text-align:center;font-family:"Tinos",serif;font-size:23px;color:var(--heading-teal);letter-spacing:1px}
  .hours{position:absolute;left:30px;top:210px;width:300px;border:2px solid #fff;border-collapse:collapse;font-size:10.5px}
  .hours td{padding:2px 6px;height:17px}
  .hours tr:nth-child(odd){background:var(--grey-row);color:#fff}
  .hours tr:nth-child(even){background:#fff;color:#333}
  .hours td:last-child{text-align:right}
  .map{left:28px;top:410px;width:140px;height:140px;border-radius:50%;border:6px solid var(--teal);background:radial-gradient(#eef0ee,#dde2df);box-shadow:0 0 0 6px rgba(255,255,255,.6)}
  .cta{position:absolute;right:22px;top:425px;text-align:right;font-family:"Quicksand",sans-serif;font-size:19px;line-height:1.25;color:#2d3b45}
  .cta strong{color:var(--deep-blue);font-weight:700;font-size:17px;letter-spacing:.5px}
  .contact .brand{position:absolute;right:22px;top:688px;z-index:1}
  .details{position:absolute;right:22px;top:738px;text-align:right;font-size:10px;line-height:1.75;color:#333;z-index:1}
  .details .num{font-weight:700}
  .details svg{vertical-align:-2px;margin-left:6px}

  /* panel: cover */
  .cover{background:linear-gradient(#fff 0%,var(--sky-top) 12%,var(--sky-mid) 40%,#fff 70%)}
  .cover .brand{position:absolute;left:28px;top:68px}
  .cover .photo{left:0;top:175px;width:360px;height:390px;background:linear-gradient(#cfe9f5 0%,#bcd3de 30%,#7a5a4a 50%,#8d8f92 70%,#b8b8b8 100%)}
  .tagline{position:absolute;left:0;right:0;top:618px;text-align:center;font-family:"Cinzel",serif;line-height:1.1}
  .tagline .l1{display:block;font-size:30px;color:#333}
  .tagline .l2{display:block;font-size:32px;color:var(--deep-blue)}
  .cover .phone{position:absolute;left:0;right:0;top:725px;text-align:center;font-size:21px;font-weight:600;color:#333}
  .cover .phone svg{vertical-align:-2px;margin-right:6px}
  .cover .addr{position:absolute;left:0;right:0;top:758px;text-align:center;font-size:10.5px;color:#333}

  /* brand name block */
  .brand{display:flex;align-items:center;gap:9px}
  .brand .dot{border-radius:50%;border:5px solid var(--teal);flex:none}
  .brand .name{font-family:"Cinzel",serif;color:var(--deep-blue);font-weight:400;line-height:1.1}
  .cover .brand .dot{width:42px;height:42px}
  .cover .brand .name{font-size:21px}
  .contact .brand .dot{width:26px;height:26px;border-width:4px}
  .contact .brand .name{font-size:13px;text-align:left}
</style>
</head>
<body>
<main class="brochure">

  <section class="panel about">
    <h2>ABOUT</h2>
    <div class="sub">Lakemont Harmony Medical, LLC</div>
    <div class="copy">
      <p>Unlike conventional medicine, which focuses on attempting to treat disease once it occurs, Lakemont Harmony Medical, LLC emphasizes improving your health in an effort to reduce the risk of pain and illness in the first place. Most people would rather be healthy and avoid illness, if they could. This is one of the main reasons for the big surge in the popularity of our wellness center.</p>
      <p>For some, Lakemont Harmony Medical, LLC will take them back to a place that is cozy and familiar, offering a rediscovery of health and wellness that had been previously known but long lost. For others, the journey may offer a new center, one never before experienced.</p>
      <p>Please take the time to meet the doctor, team, and our wellness network dedicated to helping you achieve your</p>
      <p class="tail">wellness objectives. As a patient at Lakemont Harmony Medical, LLC we will personally tailor a wellness program specifically targeted to your wellness needs using the least invasive yet highly-effective techniques and services.</p>
    </div>
    <div class="photo" role="img" aria-label="Photo of a woman meditating cross-legged on a mat outdoors in soft morning light"></div>
    <svg class="wave" height="130" viewBox="0 0 360 130" aria-hidden="true">
      <path d="M0 60 C80 20 160 30 240 60 C290 78 330 70 360 62 L360 130 L0 130Z" fill="var(--blue)"/>
      <path d="M0 80 C70 40 150 50 230 76 C290 94 330 86 360 80 L360 130 L0 130Z" fill="#fff"/>
    </svg>
  </section>

  <section class="panel contact">
    <div class="hours-title">OFFICE HOURS</div>
    <table class="hours">
      <tr><td>Monday</td><td>9</td><td>1</td></tr>
      <tr><td>Tuesday</td><td>9-12 1-4:30</td><td>1-4:30</td></tr>
      <tr><td>Wednesday</td><td>9-12 1-3</td><td>1-3</td></tr>
      <tr><td>Thursday</td><td>9-12 1-4:30</td><td>1-4:30</td></tr>
      <tr><td>Friday</td><td>9</td><td>1</td></tr>
      <tr><td>Saturday</td><td>By Appt.</td><td>Closed</td></tr>
      <tr><td>Sunday</td><td>By Appt.</td><td>Closed</td></tr>
    </table>
    <div class="photo map" role="img" aria-label="Street map showing the route to the office"></div>
    <p class="cta">To making an<br><strong>APPOINTMENT</strong><br>Contact us<br><strong>TODAY !</strong></p>
    <svg class="wave" height="300" viewBox="0 0 360 300" aria-hidden="true">
      <path d="M0 175 C100 200 180 40 360 10 L360 300 L0 300Z" fill="var(--teal)"/>
      <path d="M0 189 C110 212 190 56 360 24 L360 300 L0 300Z" fill="#fff"/>
    </svg>
    <div class="brand"><span class="dot"></span><span class="name">Lakemont Harmony<br>Medical</span></div>
    <div class="details">
      <div class="num">540-555-0172<svg width="10" height="10" viewBox="0 0 10 10"><path d="M2 1 L4 1 L4.5 3 L3.3 3.8 C4 5.3 4.7 6 6.2 6.7 L7 5.5 L9 6 L9 8 C5 8.5 1.5 5 2 1Z" fill="var(--teal)"/></svg></div>
      <div class="num">540-555-0184<svg width="10" height="10" viewBox="0 0 10 10"><rect x="1" y="3" width="8" height="5" fill="var(--teal)"/><rect x="3" y="1" width="4" height="2" fill="var(--teal)"/></svg></div>
      <div>www.lakemontharmonymedical.com<svg width="10" height="10" viewBox="0 0 10 10"><circle cx="5" cy="5" r="4" fill="none" stroke="var(--teal)" stroke-width="1.4"/><path d="M1 5H9M5 1V9" stroke="var(--teal)"/></svg></div>
      <div>48 Meadowbrook Ln Suite 210 Lakemont, VA 22790<svg width="10" height="10" viewBox="0 0 10 10"><path d="M5 1 L9.5 5 H8 V9 H2 V5 H0.5Z" fill="var(--teal)"/></svg></div>
    </div>
  </section>

  <section class="panel cover">
    <div class="brand"><span class="dot"></span><span class="name">Lakemont Harmony<br>Medical</span></div>
    <div class="photo" role="img" aria-label="Photo of the brick medical office building with its parking lot"></div>
    <svg class="wave" height="300" viewBox="0 0 360 300" aria-hidden="true">
      <path d="M0 20 C90 0 170 40 250 60 C300 72 335 60 360 40 L360 300 L0 300Z" fill="var(--teal)"/>
      <path d="M0 36 C90 18 170 52 240 70 C290 82 330 72 360 56 L360 300 L0 300Z" fill="var(--blue)"/>
      <path d="M0 44 C90 26 160 60 220 74 C270 86 320 84 360 70 L360 300 L0 300Z" fill="#fff"/>
    </svg>
    <h1 class="tagline"><span class="l1">We Create</span><span class="l2">Healthy People</span></h1>
    <div class="phone"><svg width="16" height="16" viewBox="0 0 10 10"><path d="M2 1 L4 1 L4.5 3 L3.3 3.8 C4 5.3 4.7 6 6.2 6.7 L7 5.5 L9 6 L9 8 C5 8.5 1.5 5 2 1Z" fill="var(--blue)"/></svg>540-555-0172</div>
    <div class="addr">48 Meadowbrook Ln. suite 210 Lakemont, VA 22790</div>
  </section>

</main>
</body>
</html>
```